New Company Business Card Design

I have a new company logo and I want a new business card design. I dont know if the logo file i attached is in the correct format or quality. We are a New York City Specialty construction Firm specializing in high risk out of the box projects. I want a simple and classy business card that people will his card is as crisp as the work his company does.

Target Market(s)

Clients in the heavy construction industry in New York City

Industry/Entity Type

Construction Company

Contact Information for Business Card

Simple Classy - DIFFERENT

Font styles to use
Other font styles liked:
• Mach the logo font in some way

Colors

Designer to choose colors to be used in the design.

Requirements
Must have
• Uniqueness
Nice to have
• Nothing particular - Just different and classy - Timeless
Should not have
• Goofy Shit or Gimmicky shit

```html
<!DOCTYPE html>
<html lang="en">
<head>
<meta charset="utf-8">
<title>KRT Builders, Inc. — Business Card</title>
<link href="https://fonts.googleapis.com/css2?family=Arimo:wght@400;700&display=swap" rel="stylesheet">
<style>
  :root {
    --page: #ffffff;
    --card: #6b6b6b;
    --ink: #ffffff;
    --shadow: rgba(0, 0, 0, 0.28);
  }
  html, body {
    margin: 0;
    padding: 0;
    width: 800px;
    height: 1200px;
    overflow: hidden;
    background: var(--page);
    font-family: "Arimo", Arial, sans-serif;
    color: var(--ink);
  }
  .canvas {
    position: relative;
    width: 800px;
    height: 1200px;
  }
  .card {
    position: absolute;
    left: 76px;
    width: 648px;
    height: 370px;
    background: var(--card);
    box-shadow: 0 14px 22px var(--shadow);
  }
  .card--front { top: 126px; }
  .card--back  { top: 626px; }

  /* Front: company name */
  .brand {
    position: absolute;
    left: 0;
    right: 0;
    text-align: center;
    font-weight: 700;
    color: var(--ink);
    margin: 0;
  }
  .card--front .brand__name {
    top: 112px;
    font-size: 150px;
    line-height: 1;
    letter-spacing: 6px;
  }
  .card--front .brand__suffix {
    top: 272px;
    font-size: 28px;
    line-height: 1;
    letter-spacing: 10px;
  }

  /* Back: left column */
  .identity {
    position: absolute;
    left: 0;
    top: 0;
    width: 334px;
    height: 100%;
    text-align: center;
  }
  .identity .brand__name {
    top: 44px;
    font-size: 92px;
    line-height: 1;
    letter-spacing: 4px;
  }
  .identity .brand__suffix {
    top: 146px;
    font-size: 16px;
    line-height: 1;
    letter-spacing: 6px;
  }
  .person__name {
    position: absolute;
    top: 216px;
    left: 0;
    right: 0;
    margin: 0;
    font-size: 23px;
    font-weight: 700;
    letter-spacing: 0.5px;
  }
  .person__role {
    position: absolute;
    top: 256px;
    left: 0;
    right: 0;
    margin: 0;
    font-size: 15px;
    font-weight: 700;
    letter-spacing: 0.5px;
  }
  .divider {
    position: absolute;
    left: 333px;
    top: 58px;
    width: 4px;
    height: 254px;
    background: var(--ink);
  }

  /* Back: right column */
  .contact {
    position: absolute;
    left: 337px;
    right: 0;
    top: 0;
    text-align: center;
    font-size: 16px;
    font-weight: 700;
    line-height: 19px;
  }
  .contact__group {
    position: absolute;
    left: 0;
    right: 0;
    margin: 0;
  }
  .contact__group--phone   { top: 84px; }
  .contact__group--web     { top: 165px; }
  .contact__group--address { top: 246px; font-style: normal; }
</style>
</head>
<body>
<main class="canvas">

  <section class="card card--front" aria-label="Card front">
    <p class="brand brand__name">KRT</p>
    <p class="brand brand__suffix">BUILDERS, INC.</p>
  </section>

  <section class="card card--back" aria-label="Card back">
    <div class="identity">
      <p class="brand brand__name">KRT</p>
      <p class="brand brand__suffix">BUILDERS, INC.</p>
      <h1 class="person__name">Dana Whitfield</h1>
      <p class="person__role">ENGINEER</p>
    </div>

    <div class="divider"></div>

    <div class="contact">
      <p class="contact__group contact__group--phone">+0041527830<br>+0041529146</p>
      <p class="contact__group contact__group--web">dana.whitfield@krtbuild.com<br>www.krtbuild.com</p>
      <address class="contact__group contact__group--address">48, Harbor Avenue<br>New York, USA 2190</address>
    </div>
  </section>

</main>
</body>
</html>
```